" Produção de laudos períciais para tribunais de justiça, como Perito Judicial, bem como pareceres técnicos para escritórios de advocacia e clientes diretos, na condição de Assistente Técnico, para a produção de provas, nas áreas de Informática e Documentoscopia (Grafotécnica). "

```html
<!DOCTYPE html>
<html lang="pt-BR">
<head>
<meta charset="UTF-8">
<title>Assinatura de e-mail — Vértice Perícias</title>
<link href="https://fonts.googleapis.com/css2?family=Open+Sans:wght@400;600;700&display=swap" rel="stylesheet">
<style>
  :root {
    --canvas-bg: #e9e9e9;
    --navy: #0f2d4a;
    --navy-deep: #0a2138;
    --accent-blue: #1b8fd8;
    --accent-light: #4fb3ee;
    --card-white: #ffffff;
    --text-gray: #8a8f96;
    --text-dark: #5c6168;
    --brand-silver: #d7dde3;
  }
  * { margin: 0; padding: 0; box-sizing: border-box; }
  html, body { width: 1200px; height: 1200px; overflow: hidden; }
  body {
    background: var(--canvas-bg);
    font-family: "Open Sans", Arial, sans-serif;
    position: relative;
  }
  .signature {
    position: absolute;
    left: 29px;
    top: 497px;
    width: 1040px;
    height: 211px;
    background: var(--card-white);
    border-radius: 16px;
    box-shadow: 0 2px 6px rgba(0,0,0,0.12);
    overflow: hidden;
  }
  .brand-panel {
    position: absolute;
    left: 0; top: 0;
    width: 600px;
    height: 211px;
  }
  .brand-name {
    position: absolute;
    left: 56px;
    top: 68px;
    width: 430px;
    text-align: center;
    color: var(--brand-silver);
    font-weight: 700;
    font-size: 44px;
    letter-spacing: 3px;
    line-height: 1;
    text-transform: uppercase;
  }
  .contact-block {
    position: absolute;
    left: 583px;
    top: 20px;
    width: 330px;
  }
  .person-name {
    color: var(--accent-blue);
    font-weight: 700;
    font-size: 25px;
    line-height: 1.1;
    letter-spacing: 0.3px;
  }
  .person-role {
    color: var(--text-gray);
    font-size: 12px;
    letter-spacing: 1px;
    margin-top: 3px;
    text-transform: uppercase;
  }
  .contact-row {
    display: flex;
    align-items: center;
    gap: 12px;
    margin-top: 12px;
  }
  .contact-row:first-of-type { margin-top: 14px; }
  .contact-icon {
    width: 24px; height: 24px; flex: none;
  }
  .contact-text {
    font-size: 12.5px;
    line-height: 1.3;
    color: var(--text-gray);
  }
  .contact-text strong { color: var(--text-dark); font-weight: 600; }
  .portrait-frame {
    position: absolute;
    left: 880px;
    top: 460px;
    width: 284px;
    height: 284px;
    border-radius: 50%;
    background: var(--card-white);
    box-shadow: 0 2px 6px rgba(0,0,0,0.12);
  }
  .portrait {
    position: absolute;
    left: 12px; top: 12px;
    width: 260px; height: 260px;
    border-radius: 50%;
    background: radial-gradient(circle at 55% 45%, #cfcac4 0%, #b7b3ae 45%, #7f8c6a 100%);
  }
</style>
</head>
<body>
  <section class="signature">
    <svg class="brand-panel" viewBox="0 0 600 211" aria-hidden="true">
      <path d="M0 0 H540 C500 50 500 160 540 211 H0 Z" fill="var(--navy)"/>
      <path d="M540 0 C500 50 500 160 540 211 H556 C516 160 516 50 556 0 Z" fill="var(--accent-blue)"/>
      <path d="M556 0 C524 50 524 160 556 211 H562 C530 160 530 50 562 0 Z" fill="var(--accent-light)" opacity="0.6"/>
    </svg>
    <div class="brand-name">Vértice Perícias</div>

    <div class="contact-block">
      <div class="person-name">NOME COMPLETO</div>
      <div class="person-role">Cargo ou função</div>

      <div class="contact-row">
        <svg class="contact-icon" viewBox="0 0 24 24" aria-hidden="true">
          <path d="M7 3 L10 7 L8 9.5 C9.5 12.5 11.5 14.5 14.5 16 L17 14 L21 17 L19 20.5 C11 20 4 13 3.5 5 Z" fill="var(--accent-blue)"/>
        </svg>
        <div class="contact-text">00 0000.00000<br>00 0000.00000</div>
      </div>

      <div class="contact-row">
        <svg class="contact-icon" viewBox="0 0 24 24" aria-hidden="true">
          <circle cx="12" cy="12" r="10" fill="var(--accent-blue)"/>
          <path d="M7 7 C9 8 9 10 11 10 C12 12 9 13 10 16 M15 5 C14 8 17 8 17 11 C15 12 16 15 18 16" stroke="#fff" stroke-width="1.6" fill="none"/>
        </svg>
        <div class="contact-text"><strong>verticepericias</strong>.com.br<br>contato@verticepericias.com.br</div>
      </div>

      <div class="contact-row">
        <svg class="contact-icon" viewBox="0 0 24 24" aria-hidden="true">
          <path d="M12 2 C7.5 2 5 5.5 5 9 C5 14 12 22 12 22 C12 22 19 14 19 9 C19 5.5 16.5 2 12 2 Z" fill="var(--accent-blue)"/>
          <circle cx="12" cy="9" r="2.8" fill="#fff"/>
        </svg>
        <div class="contact-text">Nome da rua, 000 - bairro<br><strong>cidade</strong> - estado - <strong>cep</strong> e país</div>
      </div>
    </div>
  </section>

  <div class="portrait-frame">
    <div class="portrait" role="img" aria-label="Foto de retrato do profissional, de terno claro e gravata vermelha"></div>
  </div>
</body>
</html>
```